LOCAL TAXI SERVICE NEEDS A BANNER AD DESIGN

NEED BANNER AD DESIGN FOR TAXI SERVICE IN NJ. WE PROVIDE LOCAL AND LONG DISTANCE TRANSPORTATION. OUR MAIN BASE OF CUSTOMER GO TO THE MAJOR AIRPORTS IN THE TRI STATE AREA. I WANT TO OFFER A SPECIAL GOING TO HOLMBRIDGE AIRPORT OF $35.00 WITH A COUPON CODE OF PW 12. THIS BANNER AD WILL BE USED FOR MY PALWIRE PAGE

Target Market(s)

PEOPLE WHO TRAVEL A LOT

Industry/Entity Type

Taxi

Font styles to use
Serif
Sans Serif

Colors
0792cd
0255a3
33a6d7
85cae6
cee9f5
ecf7fb
ffffff

Requirements
Must have
• MY COMPANY NAME: DORVAN'S TAXI

```html
<!DOCTYPE html>
<html lang="en">
<head>
<meta charset="utf-8">
<title>Dorvan's Taxi Banner</title>
<link href="https://fonts.googleapis.com/css2?family=Archivo+Black&family=Alfa+Slab+One&display=swap" rel="stylesheet">
<style>
  :root {
    --brand-deep: #0255a3;
    --brand-main: #0792cd;
    --brand-mid: #33a6d7;
    --brand-light: #85cae6;
    --brand-pale: #cee9f5;
    --brand-mist: #ecf7fb;
    --white: #ffffff;
    --title-blue: #1a6fc0;
    --ink: #111111;
    --page: #e9edf0;
  }
  html, body {
    margin: 0;
    width: 1200px;
    height: 1200px;
    overflow: hidden;
    background: var(--page);
  }
  .banner {
    position: absolute;
    left: 0;
    top: 290px;
    width: 1200px;
    height: 620px;
    background: var(--white);
    overflow: hidden;
  }
  .checker-band, .price-badge {
    position: absolute;
    left: 0;
    top: 0;
  }
  .brand-title {
    position: absolute;
    left: 112px;
    top: 40px;
    margin: 0;
    font-family: "Archivo Black", sans-serif;
    font-style: italic;
    font-size: 84px;
    line-height: 1;
    letter-spacing: 1px;
    color: var(--title-blue);
  }
  .route-line {
    position: absolute;
    left: 116px;
    top: 140px;
    margin: 0;
    font-family: "Alfa Slab One", serif;
    font-size: 33px;
    line-height: 1;
    color: var(--title-blue);
  }
  .vehicle-photo {
    position: absolute;
    left: 170px;
    top: 268px;
    width: 400px;
    height: 220px;
    border-radius: 40px 60px 20px 20px;
    background: radial-gradient(ellipse at 50% 45%, #ffffff 0%, #eef0f2 60%, #cfd3d6 100%);
  }
  .phone-block {
    position: absolute;
    left: 90px;
    top: 500px;
  }
  .toll-free {
    position: absolute;
    left: 420px;
    top: 0;
    font-family: "Archivo Black", sans-serif;
    font-size: 22px;
    line-height: 1;
    color: var(--ink);
    white-space: nowrap;
  }
  .phone-number {
    position: absolute;
    left: 0;
    top: 24px;
    font-family: "Archivo Black", sans-serif;
    font-style: italic;
    font-size: 46px;
    line-height: 1;
    color: var(--title-blue);
    white-space: nowrap;
  }
  .hours {
    position: absolute;
    left: 0;
    top: 80px;
    font-family: "Archivo Black", sans-serif;
    font-size: 20px;
    line-height: 1;
    color: var(--ink);
    white-space: nowrap;
  }
  .price {
    position: absolute;
    left: 710px;
    width: 440px;
    top: 160px;
    text-align: center;
    font-family: "Alfa Slab One", serif;
    font-size: 108px;
    line-height: 1;
    color: var(--white);
  }
  .special {
    position: absolute;
    left: 690px;
    width: 470px;
    top: 322px;
    text-align: center;
    font-family: "Alfa Slab One", serif;
    font-size: 76px;
    line-height: 1;
    color: var(--title-blue);
  }
  .coupon-note {
    position: absolute;
    left: 735px;
    width: 390px;
    top: 440px;
    margin: 0;
    text-align: center;
    font-family: "Alfa Slab One", serif;
    font-size: 26px;
    line-height: 1.15;
    color: var(--white);
  }
</style>
</head>
<body>
  <main class="banner">
    <svg class="checker-band" width="1200" height="620" viewBox="0 0 1200 620" aria-hidden="true">
      <g fill="var(--brand-deep)">
        <rect x="30" y="240" width="30" height="30" opacity="0.55"/>
        <rect x="60" y="270" width="35" height="35" opacity="0.65"/>
        <rect x="95" y="240" width="40" height="35" opacity="0.75"/>
        <rect x="135" y="275" width="45" height="45" opacity="0.8"/>
        <rect x="180" y="245" width="55" height="45" opacity="0.85"/>
        <rect x="235" y="290" width="60" height="60"/>
        <rect x="295" y="245" width="75" height="55"/>
        <rect x="415" y="240" width="105" height="95"/>
        <rect x="520" y="335" width="110" height="95"/>
        <rect x="630" y="240" width="80" height="95"/>
        <rect x="630" y="335" width="80" height="120"/>
      </g>
    </svg>

    <h1 class="brand-title">DORVAN'S TAXI</h1>
    <p class="route-line">GOING TO HOLMBRIDGE AIRPORT</p>

    <div class="vehicle-photo" role="img" aria-label="Photo of a white minivan taxi"></div>

    <div class="phone-block">
      <span class="toll-free">TOLL FREE</span>
      <span class="phone-number">1-800-555-TAXI (8294)</span>
      <span class="hours">OPEN 24 HOURS, 7 DAYS A WEEK</span>
    </div>

    <svg class="price-badge" width="1200" height="620" viewBox="0 0 1200 620" aria-hidden="true">
      <defs>
        <linearGradient id="badgeFill" x1="0" y1="0" x2="0" y2="1">
          <stop offset="0" stop-color="var(--brand-main)"/>
          <stop offset="0.5" stop-color="var(--brand-mid)"/>
          <stop offset="1" stop-color="#1f7fcc"/>
        </linearGradient>
        <linearGradient id="ribbonFill" x1="0" y1="0" x2="0" y2="1">
          <stop offset="0" stop-color="#f4f5f6"/>
          <stop offset="0.6" stop-color="#e2e4e6"/>
          <stop offset="1" stop-color="#c8cbce"/>
        </linearGradient>
      </defs>
      <path d="M910 108 Q930 98 950 108 L1120 185 Q1140 195 1140 218 L1140 445 Q1140 467 1122 480 L953 585 Q930 598 907 585 L738 480 Q720 467 720 445 L720 218 Q720 195 740 185 Z" fill="url(#badgeFill)"/>
      <path d="M680 362 L705 310 L705 362 Z" fill="#8fa3b8"/>
      <path d="M1170 362 L1145 310 L1145 362 Z" fill="#8fa3b8"/>
      <path d="M690 310 L1165 310 L1160 425 L695 425 Z" fill="url(#ribbonFill)"/>
    </svg>

    <div class="price">$35</div>
    <div class="special">special</div>
    <p class="coupon-note">AVAILABLE WITH A<br>COUPON CODE<br>OF PW 12</p>
  </main>
</body>
</html>
```